Business Card Design for Vintage Jazz

I am a vintage jazz band leader in New York City. My groups play the music of the 1920s, 1930s and 1940s. My website is morvainhale.com for more info on what I do.

I am looking for a two sided business card design that has the look and feel of a really nice business card from the 1930s. I need to convey with the design that my work has that vintage kind of class and style, but also conveys that we are fun and entertaining.

Most importantly it should make a bold staement. If Walt Pemberly had a card, what would it have looked like? I want a card that I feel confident will make an impact and will let people know that my work is te the top that NYC has to offer in vintage jazz..

Note that I have only decided to avoid the "committed payment" option as I have not used this service before. Assuming that I get quality work I will select a design from those presented.

Target Market(s)

people who want to hire my band for events, media, and new fans of the band

Industry/Entity Type

Performing Art

Contact Information for Business Card

Definitely a matte finish, possibly a sort of old style of paper with that brown tint? definitely a thick card.

Requirements
Must have
• FRONT
• My name: Tobias Merrow
• What I do: Bandleader, Guitarist, Vocalist, Songwriter
• Contact Details: morvainhale.com tobias@morvainhale.com 646-555-0184
• BACK
• My Social Media Links:
• facebook.morvainhale.com
• twitter, instagram, linkedin: morvainhale
• I'm also including a photo image I would like to use. The photo's background is not needed, and to be honest isn't really desireable. Just looking to use the image of me.
Nice to have
• I'm attaching which could be used as is, omitted from the card, or altered maybe with text going around the outside of the circle or in some other way. It may need some clean up to the edges of the lettering as we only use it for the website thumbnail.
• If there's space I'd like to include the text "join our mailing list for a free song download: freesong.morvainhale.com" If not perhaps just "Download a Free Song at: freesong.morvainhale.com - something to this end.
Should not have
• anything cartoony. Don't think retro 90s's vision of the swing era, think actual swing era!
• anything modern. Got to look old school
• Try to avoid dark backgrounds. Since we often play in bars and clubs where it is dar, a d
• avoid script fonts.

```html
<!DOCTYPE html>
<html lang="en">
<head>
<meta charset="UTF-8">
<title>Tobias Merrow — Business Card</title>
<link rel="stylesheet" href="https://fonts.googleapis.com/css2?family=Libre+Baskerville:wght@400;700&display=swap">
<style>
  :root {
    --backdrop: #d8d6d2;
    --paper-light: #f3e2a8;
    --paper-mid: #e9d28f;
    --paper-dark: #d9bd76;
    --ink: #141210;
    --ink-soft: #2a2520;
    --icon-fill: #6b5d45;
    --photo-light: #b9b4ab;
    --photo-dark: #2b2926;
  }
  * { margin: 0; padding: 0; box-sizing: border-box; }
  html, body {
    width: 1200px;
    height: 900px;
    overflow: hidden;
    background: var(--backdrop);
    font-family: "Libre Baskerville", Georgia, serif;
    color: var(--ink);
  }
  .card {
    position: absolute;
    left: 280px;
    width: 640px;
    height: 366px;
    overflow: hidden;
    background:
      radial-gradient(ellipse at 30% 40%, var(--paper-light) 0%, transparent 60%),
      radial-gradient(ellipse at 80% 85%, var(--paper-dark) 0%, transparent 55%),
      var(--paper-mid);
    box-shadow: 0 2px 6px rgba(0,0,0,0.18);
  }
  .card--back { top: 48px; }
  .card--front { top: 486px; }

  /* Back: portrait and social links */
  .portrait {
    position: absolute;
    left: 120px;
    top: 24px;
    width: 250px;
    height: 342px;
    background: linear-gradient(170deg, var(--photo-light) 0%, var(--photo-dark) 45%, var(--photo-dark) 100%);
    border-radius: 120px 120px 0 0;
  }
  .social-list {
    position: absolute;
    left: 420px;
    top: 100px;
    list-style: none;
  }
  .social-item {
    display: flex;
    align-items: center;
    height: 34px;
    font-size: 15px;
    color: var(--ink-soft);
  }
  .social-dot {
    width: 22px;
    height: 22px;
    border-radius: 50%;
    background: var(--icon-fill);
    margin-right: 12px;
    flex: none;
  }

  /* Front: mark, identity and contact */
  .mark {
    position: absolute;
    left: 70px;
    top: 66px;
    width: 160px;
    height: 160px;
    border-radius: 50%;
    background: var(--ink);
    display: flex;
    align-items: center;
    justify-content: center;
    text-align: center;
  }
  .mark-name {
    font-size: 20px;
    line-height: 1.25;
    color: var(--paper-light);
    font-weight: 400;
  }
  .divider {
    position: absolute;
    left: 258px;
    top: 82px;
    width: 1.5px;
    height: 130px;
    background: var(--ink);
  }
  .identity {
    position: absolute;
    left: 278px;
    top: 92px;
  }
  .identity-name {
    font-size: 24px;
    font-weight: 700;
    line-height: 1.2;
  }
  .identity-role {
    font-size: 14.5px;
    margin-top: 2px;
  }
  .contact {
    list-style: none;
    margin-top: 10px;
    font-size: 15px;
  }
  .contact-item {
    display: flex;
    align-items: center;
    height: 24px;
  }
  .contact-icon {
    width: 16px;
    height: 14px;
    margin-right: 8px;
    flex: none;
  }
  .site-line {
    position: absolute;
    left: 0;
    right: 0;
    top: 276px;
    display: flex;
    align-items: center;
    justify-content: center;
    gap: 24px;
  }
  .rule {
    width: 150px;
    height: 1.5px;
    background: var(--ink);
  }
  .site-url {
    font-size: 19px;
  }
</style>
</head>
<body>

<section class="card card--back">
  <div class="portrait" role="img" aria-label="Black and white photo of the bandleader in a white-trimmed blazer, tipping a boater hat"></div>
  <ul class="social-list">
    <li class="social-item"><span class="social-dot"></span>morvainhale.com</li>
    <li class="social-item"><span class="social-dot"></span>morvainhale</li>
    <li class="social-item"><span class="social-dot"></span>morvainhale</li>
    <li class="social-item"><span class="social-dot"></span>morvainhale</li>
  </ul>
</section>

<section class="card card--front">
  <div class="mark"><span class="mark-name">Tobias<br>Merrow</span></div>
  <div class="divider"></div>
  <div class="identity">
    <h1 class="identity-name">Tobias Merrow</h1>
    <p class="identity-role">Bandleader, Guitarist, Vocalist, Songwriter</p>
    <ul class="contact">
      <li class="contact-item">
        <svg class="contact-icon" viewBox="0 0 16 12" aria-hidden="true">
          <rect x="0.5" y="0.5" width="15" height="11" fill="var(--ink)"/>
          <path d="M1 1 L8 7 L15 1" fill="none" stroke="var(--paper-mid)" stroke-width="1.2"/>
        </svg>
        tobias@morvainhale.com
      </li>
      <li class="contact-item">
        <svg class="contact-icon" viewBox="0 0 16 14" aria-hidden="true">
          <path d="M1 4 Q8 -1 15 4 L13 6 L11 4.5 L5 4.5 L3 6 Z" fill="var(--ink)"/>
          <rect x="3" y="6" width="10" height="7" rx="1" fill="var(--ink)"/>
          <circle cx="8" cy="9.5" r="2" fill="var(--paper-mid)"/>
        </svg>
        646-555-0184
      </li>
    </ul>
  </div>
  <div class="site-line">
    <span class="rule"></span>
    <span class="site-url">www.morvainhale.com</span>
    <span class="rule"></span>
  </div>
</section>

</body>
</html>
```